Website for an interior designer

We need a new website for Rosa Lynn Thackery whose new business name is Rosa Lynn Thackery Interiors. She is a residential interior designer with a mix of modern and contemporary tastes. We are in the process of overhauling her website which is +15 years old and not an accurate reflection of her tastes. The uploaded photos are from some of the houses she has done as well as her logo(s). We would need a section for "About Us" that would have a paragraph of text and bullets showing services and a gallery for photos (~12 total, more to come). A contract page would be optional. The client likes the feel/look of this website: https://www.corvenhollowdesign.example/ but doesn't want to copy it exactly.

Target Market(s)

Upscale home owners

Industry/Entity Type

Interior Design

Coding

Coded - Design and coding required

Number of Pages Required

4 page

Colors

Designer to choose only greyscale colors for use in the design.

Requirements
Must have
• Home page, about us page, gallery page, contact us page.

```html
<!DOCTYPE html>
<html lang="en">
<head>
<meta charset="utf-8">
<title>Rosa Lynn Thackery Interiors</title>
<link href="https://fonts.googleapis.com/css2?family=Cinzel:wght@400;600&family=Poppins:wght@300;400;500;600&display=swap" rel="stylesheet">
<style>
:root{
  --ink:#1f1f1f;
  --text:#555555;
  --muted:#8a8a8a;
  --line:#d6d6d6;
  --panel:#eeeeee;
  --white:#ffffff;
  --dark:#333333;
}
*{box-sizing:border-box;margin:0;padding:0}
html,body{width:1200px;height:2612px;overflow:hidden;background:var(--white)}
body{position:relative;font-family:'Poppins',sans-serif;color:var(--text)}
.abs{position:absolute}
.serif{font-family:'Cinzel',serif}

/* header */
.brand{left:150px;top:14px;width:140px;text-align:center}
.brand-dot{width:26px;height:26px;border:1px solid var(--ink);border-radius:50%;margin:0 auto 6px}
.brand-name{font-family:'Cinzel',serif;font-size:10px;letter-spacing:1.5px;color:var(--ink);line-height:1.3}
.nav{left:420px;top:38px;display:flex;gap:28px;font-size:10px;letter-spacing:1px;color:var(--ink)}
.phone-box{left:880px;top:22px;width:160px;height:42px;border:2px solid var(--ink);border-radius:3px;display:flex;align-items:center;justify-content:center;gap:8px;font-weight:600;font-size:16px;color:var(--ink)}

/* hero */
.hero{left:160px;top:88px;width:880px;height:612px;background:linear-gradient(160deg,#e9e9e7 0%,#d8d6d2 45%,#a89480 60%,#cfcac4 80%,#bdbab5 100%)}
.hero-caption{left:660px;top:356px;width:340px;height:140px;background:rgba(255,255,255,.72);padding:26px 24px}
.hero-caption h1{font-family:'Cinzel',serif;font-weight:600;font-size:20px;line-height:1.3;color:var(--ink)}
.hero-caption p{font-size:11px;margin-top:8px;color:var(--dark)}
.hero-arrow{width:26px;height:26px;border-radius:50%;top:660px;display:flex;align-items:center;justify-content:center}

/* about */
.eyebrow{width:1200px;text-align:center;font-size:10px;letter-spacing:1.5px;color:var(--muted)}
.section-title{width:1200px;text-align:center;font-family:'Cinzel',serif;color:var(--ink)}
.about-title{top:780px;font-size:30px;line-height:1.25}
.about-text{left:330px;top:885px;width:540px;text-align:center;font-size:10px;line-height:1.75;color:var(--muted)}
.scroll-circle{left:580px;top:995px;width:40px;height:40px;border:1px solid var(--muted);border-radius:50%;display:flex;align-items:center;justify-content:center}

/* services */
.services{left:160px;top:1085px;width:880px;height:320px;background:var(--panel)}
.service{top:1150px;width:200px;text-align:center}
.service-icon{width:70px;height:70px;border:1px solid var(--dark);border-radius:50%;margin:0 auto 18px;display:flex;align-items:center;justify-content:center}
.service p{font-size:11px;line-height:1.6;color:var(--dark)}
.dots{left:0;top:1333px;width:1200px;display:flex;justify-content:center;gap:8px}
.dots span{width:8px;height:8px;border-radius:50%;background:#bdbdbd}
.dots span.on{background:var(--dark)}

/* gallery */
.gallery-title{top:1500px;font-size:40px}
.photo{width:340px;height:240px}
.photo-label{width:340px;text-align:center;font-size:12px;color:var(--dark)}
.btn{left:515px;top:2250px;width:170px;height:46px;border:2px solid var(--ink);display:flex;align-items:center;justify-content:center;font-family:'Cinzel',serif;font-weight:600;font-size:14px;letter-spacing:1px;color:var(--ink)}

/* footer */
.footer-rule{left:160px;top:2325px;width:880px;height:1px;background:var(--line)}
.footer{left:0;top:2345px;width:1200px;text-align:center}
.footer .brand-dot{margin-bottom:8px}
.footer .brand-name{font-size:11px}
.footer-phone{font-size:28px;font-weight:600;color:var(--ink);margin-top:28px}
.footer-mail{font-size:12px;margin-top:4px;color:var(--text)}
.socials{display:flex;justify-content:center;gap:8px;margin-top:18px}
.socials span{width:24px;height:24px;border-radius:50%;background:var(--dark)}
.copyright{font-size:9px;color:var(--muted);margin-top:18px}
</style>
</head>
<body>

<header>
  <div class="abs brand">
    <div class="brand-dot"></div>
    <div class="brand-name">ROSA LYNN THACKERY<br>INTERIORS</div>
  </div>
  <nav class="abs nav"><span>HOME</span><span>ABOUT</span><span>SERVICES</span><span>GALLERY</span><span>CONTACT</span></nav>
  <div class="abs phone-box">
    <svg width="16" height="16" viewBox="0 0 24 24" fill="none" stroke="#1f1f1f" stroke-width="2"><path d="M5 3h4l2 5-3 2a12 12 0 0 0 6 6l2-3 5 2v4a2 2 0 0 1-2 2A18 18 0 0 1 3 5a2 2 0 0 1 2-2z"/></svg>
    123 456 7890
  </div>
</header>

<section>
  <div class="abs hero" role="img" aria-label="Bright modern kitchen with a timber island, bar stools and pendant lights"></div>
  <div class="abs hero-caption">
    <h1>ROSA LYNN THACKERY INTERIORS</h1>
    <p>Work in Residential and Commercial Projects</p>
  </div>
  <div class="abs hero-arrow" style="left:966px;background:rgba(255,255,255,.85)">
    <svg width="10" height="10" viewBox="0 0 10 10"><path d="M6.5 1.5 3 5l3.5 3.5" fill="none" stroke="#333" stroke-width="1.5"/></svg>
  </div>
  <div class="abs hero-arrow" style="left:998px;background:var(--dark)">
    <svg width="10" height="10" viewBox="0 0 10 10"><path d="M3.5 1.5 7 5 3.5 8.5" fill="none" stroke="#fff" stroke-width="1.5"/></svg>
  </div>
</section>

<section>
  <div class="abs eyebrow" style="top:752px">ABOUT</div>
  <h2 class="abs section-title about-title">ROSA LYNN THACKERY<br>INTERIORS</h2>
  <p class="abs about-text">Rosa Lynn Thackery has extensive experience in all aspects of interior design. She has worked on a wide range of residential and commercial projects, bringing a modern and contemporary eye to every room. Each space is shaped around the people who live in it, with care for light, texture and lasting comfort.</p>
  <div class="abs scroll-circle">
    <svg width="12" height="12" viewBox="0 0 12 12"><path d="M2 4l4 4 4-4" fill="none" stroke="#555" stroke-width="1.3"/></svg>
  </div>
</section>

<section>
  <div class="abs services"></div>
  <div class="abs service" style="left:165px">
    <div class="service-icon"><svg width="30" height="30" viewBox="0 0 30 30" fill="none" stroke="#333" stroke-width="1.5"><circle cx="15" cy="15" r="11"/><path d="M9 21 21 9M15 9h6v6"/></svg></div>
    <p>Concept Origination and<br>Project Management</p>
  </div>
  <div class="abs service" style="left:385px">
    <div class="service-icon"><svg width="30" height="30" viewBox="0 0 30 30" fill="none" stroke="#333" stroke-width="1.5"><rect x="5" y="5" width="20" height="20"/><path d="M5 12h20M12 12v13"/></svg></div>
    <p>Review of Proposed Plans<br>for New Construction &amp;<br>Remodels</p>
  </div>
  <div class="abs service" style="left:615px">
    <div class="service-icon"><svg width="30" height="30" viewBox="0 0 30 30" fill="none" stroke="#333" stroke-width="1.5"><rect x="6" y="10" width="18" height="13"/><path d="M10 10V7h10v3M6 16h18"/></svg></div>
    <p>Procurement of Furniture,<br>Accents, Art, Fixtures and<br>Fittings</p>
  </div>
  <div class="abs service" style="left:835px">
    <div class="service-icon"><svg width="30" height="30" viewBox="0 0 30 30" fill="none" stroke="#333" stroke-width="1.5"><path d="M15 5v14M8 12l7 7 7-7M7 25h16"/></svg></div>
    <p>Selection of Fabric,<br>Finishes and Construction<br>Materials</p>
  </div>
  <div class="abs dots"><span class="on"></span><span></span><span></span></div>
</section>

<section>
  <div class="abs eyebrow" style="top:1468px">WHAT WE DO</div>
  <h2 class="abs section-title gallery-title">OUR GALLERY</h2>

  <div class="abs photo" style="left:245px;top:1578px;background:linear-gradient(135deg,#f2f2f0,#c9c6c0 60%,#6e6a64)" role="img" aria-label="Entry hall with a white staircase and round side table"></div>
  <div class="abs photo-label" style="left:245px;top:1838px">Entry</div>
  <div class="abs photo" style="left:615px;top:1578px;background:linear-gradient(135deg,#e6e4e0,#bcb6ad 55%,#8c857b)" role="img" aria-label="Open living room with sofas and tall windows"></div>
  <div class="abs photo-label" style="left:615px;top:1838px">Living Room</div>

  <div class="abs photo" style="left:245px;top:1928px;background:linear-gradient(160deg,#3e4244,#6c6f70 50%,#a6a39e)" role="img" aria-label="Study with dark ceiling and built-in shelves"></div>
  <div class="abs photo-label" style="left:245px;top:2188px">Study</div>
  <div class="abs photo" style="left:615px;top:1928px;background:linear-gradient(135deg,#f4f4f4,#dcdcdc 55%,#a9a9a9)" role="img" aria-label="White kitchen with cabinets and appliances"></div>
  <div class="abs photo-label" style="left:615px;top:2188px">Kitchen</div>

  <div class="abs btn">EXPLORE MORE</div>
</section>

<footer>
  <div class="abs footer-rule"></div>
  <div class="abs footer">
    <div class="brand-dot"></div>
    <div class="brand-name">ROSA LYNN THACKERY INTERIORS</div>
    <div class="footer-phone">123 456 7890</div>
    <div class="footer-mail">hello@rosalynnthackery.example</div>
    <div class="socials"><span></span><span></span><span></span></div>
    <div class="copyright">© Rosa Lynn Thackery · 2024 All Rights Reserved</div>
  </div>
</footer>

</body>
</html>
```